Counselling business needs a DL brochure design ready for print next week!

My business is called Clear Brook Counselling. My name is Mara Ellison and I'm a qualified Psychotherapist based in Sydney, Australia.

I need a DL brochure to promote my business. I like the idea of possibly incorporating a leaf/leaves and/or the colour green in a sophisticated, understated way in the DL design. I have attached a leaf image for reference. I am looking for a simple, elegant design overall. Not too many fonts, something which is easy to read and captures people's interest.

I need a print ready design - something that my local instant printer can use easily. I need a print ready PDF and original files too for the printer. I am anticipating that the design will be A4 folded to DL as it needs to fit into standard dimension plastic DL stands at various locations.

My business is focussed upon helping people overcome difficulties such as grief or anxiety. I also work with people to help them plan their life adventures. My business is different from the average counselling business. For example, I give my clients a beautiful thick stock postcard at the end of every session with takeaway learnings and insights which they've uncovered. That way, they can reflect upon those discoveries and capitalise upon them.

I have an office in a local wellness centre. The brochure will be showcased at the centre and in local medical centres and shops. The aim is that new prospects will pick up the brochure and be prompted to call me for a counselling appointment.

I have attached copy for my DL brochure and a competitor's DL for reference. I'm not seeking to emulate the competitor, but I thought that it could be a useful reference - the competitor DL is clear and easy to read. I need my photo to be included in the brochure, adjacent to the information about my background. I have attached a reference photo for use as a positional - a full size image will need to be dropped in as part of this job by the winning designer.

I do not have a company logo at the moment, but I need my business name and contact details repeated several times in the DL.
Updates

Hello. Thank you for your designs. I am so pleased to have received them. I will be in touch in the next 24 hours. Best, Mara

```html
<!DOCTYPE html>
<html lang="en">
<head>
<meta charset="utf-8">
<title>Clear Brook Counselling – DL Brochure</title>
<link rel="stylesheet" href="https://fonts.googleapis.com/css2?family=Jost:ital,wght@0,500;0,600;1,500;1,600&display=swap">
<style>
  :root {
    --leaf-green: #8ab63f;
    --leaf-green-soft: #a3c765;
    --ink: #3d3d3f;
    --panel-grey: #f1f1f3;
    --paper: #ffffff;
    --backdrop: #e8e5df;
    --photo-light: #cfe0a8;
    --photo-mid: #8fb25a;
    --photo-dark: #4f6e2c;
  }
  * { box-sizing: border-box; margin: 0; padding: 0; }
  html, body {
    width: 1200px;
    height: 866px;
    overflow: hidden;
    background: var(--backdrop);
    font-family: "Jost", "Futura", sans-serif;
  }
  .brochure {
    position: absolute;
    left: 55px;
    top: 48px;
    width: 1090px;
    height: 770px;
    background: var(--paper);
    box-shadow: 0 6px 18px rgba(0,0,0,0.18);
    overflow: hidden;
  }
  .brochure-art {
    position: absolute;
    inset: 0;
  }
  .panel {
    position: absolute;
    top: 0;
    height: 770px;
    width: 363px;
  }
  .panel--questions {
    left: 0;
    background: var(--leaf-green);
    color: var(--paper);
    text-align: center;
    font-style: italic;
    font-weight: 500;
  }
  .question-list {
    list-style: none;
    padding-top: 40px;
    font-size: 17.5px;
    line-height: 24px;
  }
  .question-list li { margin-bottom: 22px; }
  .question-list .lead { text-transform: uppercase; font-weight: 600; }
  .brand {
    display: flex;
    align-items: center;
    gap: 12px;
  }
  .brand-dot {
    border-radius: 50%;
    flex: none;
  }
  .brand-name {
    font-style: normal;
    font-weight: 600;
    text-transform: uppercase;
    line-height: 1.05;
  }
  .brand--questions {
    position: absolute;
    left: 62px;
    top: 678px;
  }
  .brand--questions .brand-dot { width: 70px; height: 70px; background: var(--paper); }
  .brand--questions .brand-name { font-size: 20px; color: var(--paper); }

  .panel--message { left: 363px; }
  .tagline {
    position: absolute;
    top: 302px;
    width: 100%;
    text-align: center;
    font-style: italic;
    font-weight: 500;
    font-size: 21px;
    line-height: 32px;
  }
  .tagline__main { color: var(--ink); }
  .tagline__accent { color: var(--leaf-green); margin-top: 30px; }
  .contact {
    position: absolute;
    right: 15px;
    top: 618px;
    text-align: right;
    font-style: italic;
    font-weight: 500;
    color: var(--ink);
  }
  .contact__name {
    font-style: normal;
    font-weight: 600;
    font-size: 20px;
    line-height: 1.05;
    color: var(--leaf-green);
    text-transform: uppercase;
  }
  .contact__phone { margin-top: 22px; font-size: 17px; letter-spacing: 1px; }
  .contact__web { margin-top: 14px; font-size: 17px; }
  .contact__web em { color: var(--leaf-green); }

  .panel--cover { left: 727px; }
  .brand--cover {
    position: absolute;
    left: 58px;
    top: 46px;
  }
  .brand--cover .brand-dot { width: 64px; height: 64px; background: var(--leaf-green); }
  .brand--cover .brand-name { font-size: 22px; color: var(--leaf-green); }
  .cover-headline {
    position: absolute;
    top: 680px;
    width: 100%;
    text-align: center;
    font-style: italic;
    font-weight: 600;
    font-size: 21px;
    line-height: 32px;
    color: var(--ink);
  }
  .cover-headline span { color: var(--leaf-green); }
</style>
</head>
<body>
  <main class="brochure">
    <svg class="brochure-art" width="1090" height="770" viewBox="0 0 1090 770" aria-hidden="false">
      <defs>
        <linearGradient id="photoTone" x1="0" y1="0" x2="1" y2="1">
          <stop offset="0" stop-color="var(--photo-dark)"/>
          <stop offset="0.45" stop-color="var(--photo-mid)"/>
          <stop offset="1" stop-color="var(--photo-light)"/>
        </linearGradient>
      </defs>
      <rect class="message-ground" x="363" y="0" width="364" height="770" fill="var(--panel-grey)"/>
      <rect class="cover-photo" x="727" y="130" width="363" height="500" fill="url(#photoTone)" role="img" aria-label="Photo of a woman in a green top, arms outstretched, enjoying the sun in a green park"/>
      <path class="top-cap" d="M363,0 H1090 V160 C1000,180 880,185 740,160 C600,135 470,70 385,0 Z" fill="var(--paper)"/>
      <path class="top-swoosh" d="M385,0 C470,70 600,135 740,160 C880,185 1000,180 1090,160 V182 C1000,202 880,207 740,182 C600,158 470,90 408,0 Z" fill="var(--leaf-green)"/>
      <path class="bottom-swoosh" d="M363,700 C450,620 580,570 740,565 C900,560 1000,610 1090,650 V675 C1000,640 900,590 740,590 C600,590 470,640 363,725 Z" fill="var(--leaf-green)"/>
      <path class="bottom-cap" d="M363,725 C470,640 600,590 740,590 C900,590 1000,640 1090,675 V770 H363 Z" fill="var(--paper)"/>
      <line class="fold" x1="727" y1="0" x2="727" y2="770" stroke="#e2e2e2" stroke-width="1"/>
    </svg>

    <section class="panel panel--questions">
      <ul class="question-list">
        <li><span class="lead">Do you need<br>a positive change?</span></li>
        <li><span class="lead">Do you wish</span> You felt<br>more joyful and fulfilled?</li>
        <li>You felt less stressed<br>or overwhelmed?</li>
        <li>You coped better with<br>life’s challenges?</li>
        <li>You could break<br>unhelpful habits?</li>
        <li><span class="lead">Do you imagine</span> Your<br>relationships being closer?</li>
        <li>Your life being well<br>balanced?</li>
        <li>Your goals being<br>within reach?</li>
        <li>Your life being<br>more adventurous?</li>
      </ul>
      <div class="brand brand--questions">
        <span class="brand-dot"></span>
        <span class="brand-name">Clear Brook<br>Counselling</span>
      </div>
    </section>

    <section class="panel panel--message">
      <div class="tagline">
        <p class="tagline__main">The power to create new<br>possibilities is within you.</p>
        <p class="tagline__accent">You might just need<br>a helping hand</p>
      </div>
      <address class="contact">
        <p class="contact__name">Clear Brook<br>Counselling</p>
        <p class="contact__phone">0400 517 264</p>
        <p class="contact__web">www.<em>clearbrookcounselling</em>.com</p>
      </address>
    </section>

    <section class="panel panel--cover">
      <div class="brand brand--cover">
        <span class="brand-dot"></span>
        <span class="brand-name">Clear Brook<br>Counselling</span>
      </div>
      <h1 class="cover-headline">Overcome Difficulties and<br><span>Make A Fresh Start</span></h1>
    </section>
  </main>
</body>
</html>
```